Marlowvex Website Concept

We would like a one page website. Please refer to the attached files for more information.

Please reference file attachment version 1.1.

```html
<!DOCTYPE html>
<html lang="en">
<head>
<meta charset="utf-8">
<title>Marlowvex</title>
<link rel="stylesheet" href="https://fonts.googleapis.com/css2?family=Michroma&family=Open+Sans:ital,wght@0,400;0,600;0,700;1,800&display=swap">
<style>
:root{
  --hero-deep:#0a1a28;
  --hero-blue:#1f6f95;
  --hero-red:#b3202a;
  --nav-band:#cfe0ef;
  --nav-bar:#283a4c;
  --nav-active:#4d6a82;
  --page:#f3f3f3;
  --heading:#2b4f7a;
  --text:#555;
  --tab-dark:#555;
  --tab-light:#eee;
  --label-blue:#2a5673;
  --gallery-bg:#a9a9a9;
  --footer:#2a2a2a;
  --footer-text:#d8d8d8;
  --footer-link:#5fa3d6;
  --button:#27506e;
}
*{box-sizing:border-box;margin:0;padding:0}
html,body{width:1200px;height:1000px;overflow:hidden}
body{position:relative;font-family:"Open Sans",Arial,sans-serif;color:var(--text);background:var(--page)}
.abs{position:absolute}
.photo{position:absolute}
.hero{left:0;top:0;width:1200px;height:130px;background:linear-gradient(100deg,#0b2a3e 0%,#1c5a7a 25%,#0b1e2e 45%,#6a1a22 55%,#0c2232 70%,#1b6a8e 90%,#0a2030 100%)}
.logo-box{left:460px;top:14px;width:282px;height:28px;background:#f4f4f4;border:1px solid #999;display:flex;align-items:center;justify-content:center;gap:8px}
.logo-box .mark{width:12px;height:12px;border-radius:50%;background:var(--heading)}
.logo-box .name{font-family:"Michroma",sans-serif;font-size:15px;color:var(--heading);letter-spacing:1px}
.hero-title{left:0;top:48px;width:1200px;text-align:center;font-style:italic;font-weight:800;font-size:19px;letter-spacing:2px;color:#fff}
.hero-sub{left:300px;top:68px;width:600px;text-align:center;font-size:6px;line-height:8px;color:#cde}
.arrow{top:62px;width:27px;height:13px;background:#f2f2f2;display:flex;align-items:center;justify-content:center}
.nav-band{left:0;top:130px;width:1200px;height:12px;background:var(--nav-band)}
.nav{left:150px;top:130px;width:900px;height:12px;background:var(--nav-bar);display:flex;align-items:center;font-size:6px;color:#dde;letter-spacing:.5px}
.nav span{padding:0 16px;line-height:12px}
.nav .active{background:var(--nav-active);padding:0 22px}
.tab{height:10px;width:160px;background:linear-gradient(90deg,var(--tab-dark),var(--tab-light));font-family:"Michroma",sans-serif;font-size:8px;color:#fff;padding-left:12px;line-height:10px;letter-spacing:1px}
.subhead{height:9px;border:1px solid #ccc;background:#fafafa;font-family:"Michroma",sans-serif;font-size:7px;line-height:8px;color:var(--heading);padding-left:12px;letter-spacing:.5px}
.body-text{font-size:5.5px;line-height:6.5px;color:#666}
.diff-head{font-family:"Michroma",sans-serif;font-size:8.5px;color:var(--heading);letter-spacing:1px;font-weight:700}
.pager{width:20px;height:8px;border:1px solid #ccc;background:#eee}
.badge{height:30px;background:#fff;border:1px solid #ddd;display:flex;align-items:center;justify-content:center}
.badge i{display:block;width:26px;height:26px;border-radius:50%}
.mission{left:0;top:368px;width:1200px;height:117px;background:linear-gradient(90deg,#bfc4c6 0%,#e6e6e2 30%,#d6d6d0 60%,#c6bfb4 85%,#c88a60 100%)}
.list-item{font-size:6px;color:#333;left:202px}
.dot{left:152px;width:34px;height:8px;background:#333;border-radius:4px}
.value-panel{left:665px;top:415px;width:385px;height:63px;background:rgba(110,110,110,.75)}
.value-tabs{display:flex;gap:4px;padding:2px}
.value-tabs span{flex:1;font-size:6px;color:#eee;background:rgba(255,255,255,.2);text-align:center;line-height:8px}
.services{left:0;top:485px;width:1200px;height:190px;background:#fff}
.label{width:145px;height:7px;background:var(--label-blue);font-family:"Michroma",sans-serif;font-size:6px;line-height:7px;color:#fff;padding-left:32px}
.caption{position:absolute;left:0;right:0;bottom:0;height:6px;background:rgba(0,0,0,.55);font-size:4.5px;color:#fff;padding-left:22px;line-height:6px}
.gallery{left:0;top:675px;width:1200px;height:165px;background:linear-gradient(90deg,#8d8d8d,#cfcfcf 50%,#8d8d8d)}
.filter{top:703px;height:10px;border:1px solid #777;background:#c9c9c9;font-family:"Michroma",sans-serif;font-size:6px;line-height:8px;text-align:center;color:#234}
.footer{left:0;top:840px;width:1200px;height:160px;background:var(--footer)}
.f-text{font-size:6px;color:var(--footer-text);letter-spacing:.3px}
.f-label{font-size:6px;color:var(--footer-text)}
.req{color:#d33}
.input{left:308px;width:168px;height:8px;background:#3a3a3a;border:1px solid #555}
.btn{height:8px;background:var(--button);font-size:6px;color:#fff;text-align:center;line-height:8px}
.f-link{font-size:6px;color:var(--footer-link)}
</style>
</head>
<body>

<!-- Hero -->
<section class="abs hero" role="img" aria-label="Digital security backdrop with padlocks over data streams"></section>
<div class="abs logo-box"><span class="mark"></span><span class="name">MARLOWVEX</span></div>
<h1 class="abs hero-title">LOREM IPSUM IS SIMPLY DUMMY</h1>
<p class="abs hero-sub">Lorem ipsum is simply dummy text of the printing and typesetting industry. Lorem ipsum has been the industry standard dummy text ever since the 1500s.</p>
<div class="abs arrow" style="left:25px"><svg width="8" height="8" viewBox="0 0 8 8"><path d="M5 1 2 4l3 3" fill="none" stroke="#1f6f95" stroke-width="1.5"/></svg></div>
<div class="abs arrow" style="left:1127px"><svg width="8" height="8" viewBox="0 0 8 8"><path d="M3 1l3 3-3 3" fill="none" stroke="#1f6f95" stroke-width="1.5"/></svg></div>

<!-- Navigation -->
<div class="abs nav-band"></div>
<nav class="abs nav"><span class="active">HOME</span><span>ABOUT US</span><span>MISSION</span><span>SERVICES AND TRAINING</span><span>GALLERY</span><span>CONTACT US</span></nav>

<!-- About -->
<div class="abs tab" style="left:150px;top:151px">ABOUT US</div>
<div class="photo" style="left:150px;top:172px;width:225px;height:53px;background:linear-gradient(90deg,#eee,#c9b89a 50%,#eee);border:1px solid #ccc" role="img" aria-label="Team of three security staff in uniform"></div>
<div class="abs subhead" style="left:415px;top:181px;width:610px">COMPANY PROFILE (SDVOSB)</div>
<p class="abs body-text" style="left:415px;top:192px;width:610px">Lorem ipsum is simply dummy text of the printing and typesetting industry. Lorem ipsum has been the standard dummy text ever since the 1500s, when an unknown printer took a galley of type. It has survived not only five centuries, but also the leap into electronic typesetting. You've visited this page many times.</p>
<div class="abs subhead" style="left:150px;top:236px;width:590px">LOREM IPSUM</div>
<p class="abs body-text" style="left:150px;top:246px;width:580px">Lorem ipsum is simply dummy text of the printing and typesetting industry. Lorem ipsum has been the industry standard dummy text ever since the 1500s, when an unknown printer took a galley of type and scrambled it to make a type specimen book. It has survived not only five centuries, but also the leap into electronic typesetting, remaining essentially unchanged. It was popularised with sheets containing passages, and more recently with publishing software including versions of lorem ipsum text.</p>
<div class="photo" style="left:826px;top:238px;width:224px;height:50px;background:linear-gradient(90deg,#6a5a52,#a2463e 50%,#4a4440)" role="img" aria-label="Instructor at a firing range"></div>

<div class="abs diff-head" style="left:158px;top:296px">THE MARLOWVEX DIFFERENCE</div>
<div class="abs pager" style="left:507px;top:296px"></div><div class="abs pager" style="left:540px;top:296px"></div>
<div class="photo" style="left:150px;top:308px;width:200px;height:30px;background:linear-gradient(90deg,#6c5a4c,#a49078)" role="img" aria-label="Students in a training class"></div>
<div class="photo" style="left:365px;top:308px;width:200px;height:30px;background:linear-gradient(90deg,#8a96a4,#505a66)" role="img" aria-label="Helicopter on an airfield"></div>
<p class="abs body-text" style="left:150px;top:340px;width:415px">Our instructors are State Certified instructors for Pistol, Rifle, Personal Protection in the Home, Range Safety Officers, and licensed Concealed Carry Handgun Instructors.</p>

<div class="abs diff-head" style="left:617px;top:296px">THE MARLOWVEX DIFFERENCE</div>
<div class="abs pager" style="left:990px;top:296px"></div><div class="abs pager" style="left:1028px;top:296px"></div>
<div class="abs badge" style="left:612px;top:308px;width:145px"><i style="background:#2a3f7a"></i></div>
<div class="abs badge" style="left:762px;top:308px;width:135px"><i style="background:#6ab0e0"></i></div>
<div class="abs badge" style="left:912px;top:308px;width:135px"><i style="background:#3a3a3a"></i></div>
<p class="abs body-text" style="left:617px;top:340px;width:430px">Marlowvex delivers the unmatched tactical experience of seasoned Special Forces Operators, combined with unique field and ground based logistical support, to ensure our customers' needs are satisfied to the highest standards possible.</p>

<!-- Mission -->
<section class="abs mission" role="img" aria-label="Soft focus office interior backdrop"></section>
<div class="abs tab" style="left:150px;top:378px">MISSION</div>
<p class="abs body-text" style="left:250px;top:390px;width:700px;text-align:center;color:#333">Marlowvex's mission is to provide our customers with the highest level of Special Operations training and support. At Marlowvex we accomplish our mission by adhering to our core values of loyalty, integrity and honor.</p>
<div class="abs dot" style="top:410px"></div><div class="abs dot" style="top:420px"></div><div class="abs dot" style="top:430px"></div>
<p class="abs list-item" style="top:409px">Loyalty - To our employees</p>
<p class="abs list-item" style="top:418px">Loyalty - To our customers</p>
<p class="abs list-item" style="top:427px">Loyalty - To our employers</p>
<p class="abs list-item" style="top:437px">Loyalty - To our employees</p>
<p class="abs body-text" style="left:202px;top:445px;width:215px;color:#333">Our employees are our most valued assets. Their trust is earned every day through respect and fair treatment.</p>
<svg class="abs" style="left:440px;top:418px" width="180" height="44" viewBox="0 0 180 44">
  <line x1="0" y1="22" x2="180" y2="22" stroke="#555" stroke-width="1"/>
  <ellipse cx="90" cy="22" rx="76" ry="20" fill="#444"/>
  <ellipse cx="90" cy="22" rx="70" ry="17" fill="#bbb"/>
  <ellipse cx="90" cy="22" rx="24" ry="10" fill="#eee" stroke="#666"/>
  <text x="90" y="12" font-size="6" text-anchor="middle" fill="#222" font-family="Open Sans, sans-serif">Loyalty</text>
  <text x="90" y="38" font-size="6" text-anchor="middle" fill="#222" font-family="Open Sans, sans-serif">Honor</text>
  <text x="40" y="24" font-size="5" text-anchor="middle" fill="#222" font-family="Open Sans, sans-serif">Integrity</text>
  <text x="140" y="24" font-size="5" text-anchor="middle" fill="#222" font-family="Open Sans, sans-serif">Service</text>
</svg>
<div class="abs value-panel">
  <div class="value-tabs"><span>Integrity</span><span>Commitment</span><span>Honor</span></div>
  <p class="body-text" style="color:#eee;padding:2px 22px">Lorem ipsum is simply dummy text of the printing and typesetting industry. Lorem ipsum has been the standard dummy text ever since the 1500s, when an unknown printer took a galley of type and scrambled it to make a specimen book. It has survived not only five centuries, but also the leap into electronic typesetting, remaining essentially unchanged.</p>
</div>

<!-- Services and training -->
<section class="abs services"></section>
<div class="abs tab" style="left:150px;top:495px;width:260px">SERVICES AND TRAINING</div>
<div class="abs label" style="left:150px;top:520px">SERVICES</div>
<div class="photo" style="left:150px;top:532px;width:207px;height:34px;background:linear-gradient(90deg,#2a2e36,#6a6e78)" role="img" aria-label="Close protection team beside vehicles"><span class="caption">LOREM IPSUM IS SIMPLY</span></div>
<div class="photo" style="left:381px;top:532px;width:207px;height:34px;background:linear-gradient(90deg,#3a6ab0,#c9b08a)" role="img" aria-label="Training staff group"><span class="caption">LOREM IPSUM IS SIMPLY</span></div>
<div class="photo" style="left:612px;top:532px;width:208px;height:34px;background:linear-gradient(90deg,#5a4a3c,#a8a090)" role="img" aria-label="Field training exercise"><span class="caption">LOREM IPSUM IS SIMPLY</span></div>
<div class="photo" style="left:843px;top:532px;width:207px;height:34px;background:linear-gradient(180deg,#c8a878,#6a5a44)" role="img" aria-label="Helicopter at dusk"><span class="caption">LOREM IPSUM IS SIMPLY</span></div>
<div class="abs label" style="left:150px;top:573px">SERVICES</div>
<div class="photo" style="left:150px;top:590px;width:207px;height:32px;background:linear-gradient(90deg,#3a3e48,#7a7e88)" role="img" aria-label="Security vehicle escort"><span class="caption">LOREM IPSUM IS SIMPLY</span></div>
<div class="photo" style="left:381px;top:590px;width:207px;height:32px;background:linear-gradient(90deg,#9aa088,#d8d0b8)" role="img" aria-label="Tactical drill outdoors"><span class="caption">LOREM IPSUM IS SIMPLY</span></div>
<div class="photo" style="left:150px;top:628px;width:207px;height:34px;background:linear-gradient(90deg,#4a4a52,#8a8a92)" role="img" aria-label="Classroom instruction"><span class="caption">LOREM IPSUM IS SIMPLY</span></div>
<div class="photo" style="left:381px;top:628px;width:207px;height:34px;background:linear-gradient(90deg,#3a4a5a,#8a9aa8)" role="img" aria-label="Defensive tactics session"><span class="caption">LOREM IPSUM IS SIMPLY</span></div>
<div class="photo" style="left:605px;top:588px;width:445px;height:74px;background:linear-gradient(90deg,#8a9aa8,#d8a898 40%,#c06a5a 70%,#7a6a6a);border-bottom:10px solid #b3202a" role="img" aria-label="Self defence training demonstration"></div>

<!-- Gallery -->
<section class="abs gallery" role="img" aria-label="Grey city skyline backdrop"></section>
<div class="abs tab" style="left:150px;top:684px">GALLERY</div>
<div class="abs filter" style="left:395px;width:80px">ALL</div>
<div class="abs filter" style="left:500px;width:110px">SERVERS</div>
<div class="abs filter" style="left:640px;width:110px">OFFICES</div>
<div class="abs filter" style="left:778px;width:70px">ELSE</div>
<div class="photo" style="left:150px;top:720px;width:212px;height:34px;background:linear-gradient(90deg,#7a7668,#b8b4a4)" role="img" aria-label="Team in uniform outdoors"></div>
<div class="photo" style="left:380px;top:720px;width:100px;height:34px;background:#b3301e" role="img" aria-label="Company banner"></div>
<div class="photo" style="left:480px;top:720px;width:345px;height:34px;background:linear-gradient(90deg,#4a8a3a,#7a6a50 60%,#8a7a60)" role="img" aria-label="Training in the field"></div>
<div class="photo" style="left:838px;top:720px;width:212px;height:34px;background:linear-gradient(90deg,#c8c8d8,#6a6a50)" role="img" aria-label="Group with flag"></div>
<div class="photo" style="left:150px;top:758px;width:212px;height:34px;background:linear-gradient(90deg,#8a7a5a,#c0b8a0)" role="img" aria-label="Group photo with flag"></div>
<div class="photo" style="left:380px;top:758px;width:212px;height:34px;background:linear-gradient(90deg,#8a6a4a,#c8a47a)" role="img" aria-label="Desert exercise"></div>
<div class="photo" style="left:608px;top:758px;width:212px;height:72px;background:linear-gradient(180deg,#c8c4b8,#3a3a3a)" role="img" aria-label="Officer portrait"></div>
<div class="photo" style="left:838px;top:758px;width:212px;height:34px;background:linear-gradient(90deg,#8a8a78,#b84a4a 50%,#6a6a58)" role="img" aria-label="Training exercise"></div>
<div class="photo" style="left:150px;top:797px;width:442px;height:33px;background:linear-gradient(90deg,#d8d8d8,#3a4458 40%,#d8d8d8)" role="img" aria-label="Officers lined up"></div>
<div class="photo" style="left:838px;top:797px;width:212px;height:33px;background:linear-gradient(90deg,#9a9aa8,#5a5a6a)" role="img" aria-label="Classroom group"></div>

<!-- Contact -->
<footer class="abs footer"></footer>
<div class="abs tab" style="left:150px;top:850px;background:linear-gradient(90deg,#111,#555)">CONTACT</div>
<p class="abs f-text" style="left:150px;top:871px;width:200px;line-height:7px">CREATE AN ACCOUNT TO FILE YOUR INCOME TAX RETURNS</p>
<p class="abs f-text" style="left:150px;top:888px">PLEASE PROVIDE THE FOLLOWING INFORMATION TO SIGN UP:</p>
<p class="abs f-text" style="left:598px;top:893px"><span class="req">*</span> MANDATORY</p>
<p class="abs f-label" style="left:150px;top:900px">Username<span class="req">*</span></p>
<p class="abs f-label" style="left:150px;top:910px">Password (min. 6 char)<span class="req">*</span></p>
<p class="abs f-label" style="left:150px;top:920px">Confirm Password<span class="req">*</span></p>
<p class="abs f-label" style="left:150px;top:931px">Email ID<span class="req">*</span></p>
<p class="abs f-label" style="left:150px;top:941px">Mobile<span class="req">*</span></p>
<p class="abs f-label" style="left:150px;top:951px;line-height:6px">Verification code<br>(as seen in the image)</p>
<div class="abs input" style="top:900px"></div>
<div class="abs input" style="top:910px"></div>
<div class="abs input" style="top:921px"></div>
<div class="abs input" style="top:931px"></div>
<div class="abs input" style="top:941px"></div>
<p class="abs f-label" style="left:485px;top:900px">Check Availability</p>
<p class="abs" style="left:360px;top:950px;font-size:9px;color:#ccc;letter-spacing:2px">124132</p>
<p class="abs f-label" style="left:485px;top:950px">Refresh</p>
<div class="abs" style="left:312px;top:965px;width:6px;height:6px;background:#ddd"></div>
<p class="abs f-label" style="left:322px;top:964px;width:170px;line-height:6.5px">I agree to the Terms of Service and have read and understood the Privacy Policy</p>
<div class="abs btn" style="left:312px;top:982px;width:148px">CREATE ACCOUNT</div>

<p class="abs f-text" style="left:738px;top:876px">HAVE AN ACCOUNT?</p>
<div class="abs btn" style="left:738px;top:885px;width:90px">SIGN UP</div>
<p class="abs f-label" style="left:738px;top:895px;color:#999">I forgot my password</p>
<p class="abs f-link" style="left:738px;top:920px">Address :</p>
<p class="abs f-label" style="left:738px;top:926px;line-height:7px">118 Larkfield Hollow Rd, Brenton, NC 28990<br>United States</p>
<p class="abs f-link" style="left:738px;top:940px">Contact No.:</p>
<p class="abs f-label" style="left:738px;top:946px">(555) 014-2290</p>
<p class="abs f-link" style="left:738px;top:952px">Email Id:</p>
<p class="abs f-label" style="left:738px;top:958px">info@marlowvexgroup.com</p>
<p class="abs f-label" style="left:738px;top:978px;color:#888">All copyright 2014</p>
</body>
</html>
```